OM sidrawi Multibrand Web Design

We need Simple but very Elegant Website for Our Middle East Company based in Kuwait, We are not good in describing design but we need simple but elegant and responsive to attract new market and to enable us competing in business

It Company

```html
<!DOCTYPE html>
<html lang="en">
<head>
<meta charset="utf-8">
<title>Landing Page</title>
<link href="https://fonts.googleapis.com/css2?family=Arimo:wght@400;700&display=swap" rel="stylesheet">
<style>
  :root {
    --bg: #f4f4f4;
    --page: #fafafa;
    --rule: #e2e2e2;
    --heading: #3d3d3d;
    --body: #7d7d7d;
    --muted: #a3a3a3;
    --accent: #c8472b;
    --icon-bg: #d4d4d4;
    --icon-fg: #ffffff;
  }
  * { box-sizing: border-box; margin: 0; padding: 0; }
  html, body { width: 1200px; height: 1200px; overflow: hidden; background: var(--bg); }
  body { font-family: "Arimo", Arial, sans-serif; position: relative; }

  .page {
    position: absolute; left: 0; top: 110px;
    width: 1280px; height: 1045px;
    background: var(--page);
    transform: scale(0.9375); transform-origin: top left;
  }
  .hero { position: absolute; left: 116px; top: 31px; display: flex; gap: 2px; }
  .hero__photo { width: 347px; height: 276px; }
  .hero__photo--city { background: linear-gradient(180deg, #3f83b8 0%, #8fb3c6 45%, #5a5a55 75%, #3a3a38 100%); }
  .hero__photo--port { background: linear-gradient(135deg, #b9a88a 0%, #a99a80 35%, #5d6f86 55%, #8e7e72 75%, #a49786 100%); }
  .hero__photo--plant { background: linear-gradient(180deg, #c86a4a 0%, #d58a7a 30%, #7b6f86 60%, #c9c3c8 80%, #4a5a7a 100%); }

  .rule { position: absolute; left: 0; width: 1272px; height: 2px; background: var(--rule); }
  .rule--top { top: 493px; }
  .rule--bottom { top: 1028px; width: 1280px; }

  .about { position: absolute; left: 124px; top: 560px; width: 477px; text-align: right; }
  .about__title { font-size: 29px; font-weight: 700; letter-spacing: 1px; color: var(--heading); }
  .divider { display: block; margin: 36px 0 0 auto; }
  .about__text { margin-top: 36px; font-size: 12.5px; line-height: 21px; color: var(--body); }
  .about__text p + p { margin-top: 11px; }
  .about__text strong { color: var(--accent); }
  .divider--low { margin-top: 38px; }
  .btn {
    display: inline-flex; align-items: center; gap: 4px;
    margin-top: 38px; width: 193px; height: 45px; justify-content: center;
    border: 1px solid var(--rule); background: #fff;
    font-size: 13px; color: var(--body);
  }

  .features { position: absolute; left: 665px; top: 564px; }
  .features__line { position: absolute; left: 30px; top: 64px; height: 300px; border-left: 1px dashed var(--rule); }
  .feature { position: relative; height: 117px; padding-left: 94px; }
  .feature__icon {
    position: absolute; left: 0; top: 0; width: 64px; height: 64px; border-radius: 50%;
    background: var(--icon-bg); display: flex; align-items: center; justify-content: center;
  }
  .feature__title { padding-top: 3px; font-size: 18px; font-weight: 700; color: var(--heading); }
  .feature__text { margin-top: 8px; width: 390px; font-size: 12.5px; line-height: 21px; color: var(--muted); }
  .feature__text strong { color: var(--accent); }
</style>
</head>
<body>
<main class="page">
  <section class="hero">
    <div class="hero__photo hero__photo--city" role="img" aria-label="Hazy city skyline with tall towers"></div>
    <div class="hero__photo hero__photo--port" role="img" aria-label="Aerial view of a container ship at a port"></div>
    <div class="hero__photo hero__photo--plant" role="img" aria-label="Refinery with tanks at sunset"></div>
  </section>

  <div class="rule rule--top"></div>

  <section class="about">
    <h2 class="about__title">ABOUT US</h2>
    <svg class="divider" width="156" height="10" viewBox="0 0 156 10"><line x1="0" y1="5" x2="148" y2="5" stroke="#dcdcdc"/><circle cx="151" cy="5" r="3.5" fill="none" stroke="#dcdcdc"/></svg>
    <div class="about__text">
      <p>Lorem ipsum dolor sit amet, consectetuer <strong>adipiscing elit</strong>. Aenean commodo ligula<br>eget dolor. Aenean massa.</p>
      <p>Nulla consequat massa quis enim.<br>Donec pede justo, fringilla vel, aliquet nec, vulputate eget, arcu.<br>In enim justo, rhoncus ut, imperdiet a, venenatis vitae, justo. Nullam dictum felis eu<br>pede mollis pretium.<br>Integer tincidunt. Cras dapibus. Vivamus elementum semper nisi.<br>Aenean <strong>vulputate</strong> eleifend tellus.</p>
    </div>
    <svg class="divider divider--low" width="156" height="10" viewBox="0 0 156 10"><line x1="0" y1="5" x2="148" y2="5" stroke="#dcdcdc"/><circle cx="151" cy="5" r="3.5" fill="none" stroke="#dcdcdc"/></svg>
    <a class="btn"><svg width="14" height="12" viewBox="0 0 14 12" fill="#888"><circle cx="5" cy="3" r="2.5"/><path d="M0 11c0-3 2-5 5-5s5 2 5 5z"/><circle cx="10" cy="3.5" r="2"/><path d="M10 6.5c2 0 4 1.5 4 4.5h-3c0-2-.5-3.5-1-4.5z"/></svg>Check out our Team</a>
  </section>

  <section class="features">
    <div class="features__line"></div>
    <article class="feature">
      <div class="feature__icon"><svg width="30" height="30" viewBox="0 0 30 30" stroke="#fff" stroke-width="3" fill="none" stroke-linecap="round"><path d="M6 24L20 10M10 6l14 14"/><path d="M20 10l4-4" /><path d="M6 8l4-4 3 3-4 4z" fill="#fff"/></svg></div>
      <h3 class="feature__title">CRAFTED WITH LOVE</h3>
      <p class="feature__text">Aenean vulputate eleifend tellus. Aenean leo ligula, porttitor eu,<br>consequat vitae, eleifend ac, enim. Aliquam lorem ante, dapibus in.</p>
    </article>
    <article class="feature">
      <div class="feature__icon"><svg width="24" height="32" viewBox="0 0 24 32" fill="#fff"><rect x="12" y="3" width="3" height="21"/><path d="M15 3c2 4 7 5 6 11-1-4-4-5-6-6z"/><ellipse cx="9" cy="24" rx="6" ry="4.5"/></svg></div>
      <h3 class="feature__title">MELODICAL BY NATURE</h3>
      <p class="feature__text">Donec vitae sapien ut libero venenatis faucibus. Nullam quis ante.<br>Etiam sit amet orci eget eros faucibus tincidunt.</p>
    </article>
    <article class="feature">
      <div class="feature__icon"><svg width="16" height="28" viewBox="0 0 16 28" fill="#fff"><path d="M10 2L3 16h5l-2 10 8-15H9z"/></svg></div>
      <h3 class="feature__title">LIGHTNING FAST</h3>
      <p class="feature__text">Donec sodales sagittis magna. Sed consequat, leo eget bibendum<br>sodales, augue velit cursus nunc, quis gravida magna mi a libero.</p>
    </article>
    <article class="feature">
      <div class="feature__icon"><svg width="30" height="30" viewBox="0 0 30 30" fill="#fff"><rect x="6" y="6" width="3" height="20" transform="rotate(-15 7 16)"/><path d="M9 6c5-2 8 3 15 0l-3 10c-6 3-9-2-14 0z"/></svg></div>
      <h3 class="feature__title">FREAKY FLAGS</h3>
      <p class="feature__text">Nullam quis ante. Etiam sit <strong>amet orci eget</strong> eros faucibus<br>tincidunt. Donec vitae sapien ut libero venenatis faucibus.</p>
    </article>
  </section>

  <div class="rule rule--bottom"></div>
</main>
</body>
</html>
```